Brookvale RV and Spa Service Van Wrap Design

Brookvale RV Repair and Spa Vehicle Wrap Design

Project goal: To design a vehicle wrap for a service van that aligns with existing branding and logos of Brookvale RV Repair and Spa.
Scope of work: - Design a vehicle wrap that incorporates Brookvale RV Repair and Spa’s branding and logos. - Ensure the design highlights services such as Maintenance & Repair, Oil Change & Lube, Slide Outs & Awnings, Tires & Brakes, RV Spa & Detailing, Leveling Systems, AC & Heating. - Create a visually appealing and informative wrap that effectively communicates the services and professionalism of certified techs. Company phone number (888) 514-2089 and website www.brookvalerv.example

Fonts: Gotham HTF medium and Gotham HTF Book
Pantones: 320 C and Cool Gray 9 C
#009ca6 and #75787b

Target Market(s)

RV Owners

Industry/Entity Type

RV Repair and RV Spa

Font styles to use
• Gotham HTF

Colors
00AB8E
00BBA5
67D7C9
C6EFE9
E9F9F6

Requirements
Must have
• Our fonts, logo, brand colors, list of services, contact information. Halvorn Transit Long Van is the vehicle.
Nice to have
• Eye-catching design, with an emphasis on "RV Repair & Spa" to generate interest in our services (make that the largest part of the design.
Should not have
• Do not include the person in the design.

```html
<!DOCTYPE html>
<html lang="en">
<head>
<meta charset="utf-8">
<title>Brookvale RV Repair and Spa – Van Wrap</title>
<link rel="stylesheet" href="https://fonts.googleapis.com/css2?family=Montserrat:wght@400;600;700&family=Oswald:wght@500&display=swap">
<style>
  :root {
    --teal: #009ca6;
    --gray: #75787b;
    --gray-light: #a7a9ab;
    --white: #f4f5f5;
    --black: #141414;
    --tyre: #1d1d1d;
    --rim: #c9cbcd;
    --glass: #cfd2d4;
    --trim: #2a2a2a;
  }
  html, body {
    margin: 0;
    width: 1200px;
    height: 1200px;
    overflow: hidden;
    background: #ffffff;
  }
  .wrap-sheet { display: block; width: 1200px; height: 1200px; }
  .brand-name { font-family: "Montserrat", sans-serif; font-weight: 700; fill: var(--teal); }
  .phone { font-family: "Oswald", sans-serif; font-weight: 500; font-size: 21px; fill: var(--gray); }
  .van-dark .phone { fill: var(--gray-light); }
  .website { font-family: "Montserrat", sans-serif; font-weight: 600; font-size: 10px; fill: var(--teal); letter-spacing: 0.5px; }
  .service { font-family: "Oswald", sans-serif; font-weight: 500; font-size: 9px; fill: #ffffff; }
</style>
</head>
<body>
<svg class="wrap-sheet" viewBox="0 0 960 960" xmlns="http://www.w3.org/2000/svg">
  <defs>
    <clipPath id="van-body">
      <path d="M128,70 Q130,48 160,46 L655,46 Q690,50 720,78 L775,130 Q800,142 830,152 Q846,160 848,190 L848,232 Q848,242 838,242 L120,242 Q116,242 116,230 L118,90 Z"/>
    </clipPath>

    <g id="body-outline">
      <path d="M128,70 Q130,48 160,46 L655,46 Q690,50 720,78 L775,130 Q800,142 830,152 Q846,160 848,190 L848,232 Q848,242 838,242 L120,242 Q116,242 116,230 L118,90 Z" fill="none" stroke="#9a9c9e" stroke-width="1"/>
    </g>

    <g id="door-seams">
      <line x1="385" y1="50" x2="385" y2="236" stroke="#777" stroke-width="1" opacity="0.45"/>
      <line x1="465" y1="50" x2="465" y2="236" stroke="#777" stroke-width="1" opacity="0.45"/>
      <line x1="570" y1="50" x2="570" y2="236" stroke="#777" stroke-width="1" opacity="0.45"/>
    </g>

    <g id="van-hardware">
      <path class="side-window" d="M578,72 L650,72 Q668,74 690,96 L712,120 L578,122 Z" fill="var(--glass)" stroke="var(--trim)" stroke-width="3"/>
      <path class="windscreen" d="M700,70 Q720,82 770,128 L760,130 Q730,100 700,78 Z" fill="#3b3d3f"/>
      <rect x="676" y="118" width="16" height="22" rx="3" fill="var(--trim)"/>
      <line x1="748" y1="40" x2="750" y2="130" stroke="var(--trim)" stroke-width="1.5"/>
      <rect x="802" y="158" width="26" height="42" rx="3" fill="#dcdcdc" stroke="#888" stroke-width="1"/>
      <rect x="806" y="184" width="18" height="10" fill="#e88a1a"/>
      <rect x="828" y="165" width="20" height="36" fill="#3a3a3a"/>
      <rect x="790" y="204" width="62" height="20" rx="4" fill="#c7c9cb"/>
      <rect x="114" y="212" width="30" height="22" rx="3" fill="#b9bbbd"/>
      <rect x="130" y="86" width="10" height="32" fill="#c0392b"/>
      <rect x="565" y="136" width="5" height="16" rx="2" fill="#333"/>
      <path d="M208,242 A50,50 0 0 1 308,242 Z" fill="#101010"/>
      <path d="M680,242 A50,50 0 0 1 780,242 Z" fill="#101010"/>
      <g class="wheel">
        <circle cx="258" cy="245" r="42" fill="var(--tyre)"/>
        <circle cx="258" cy="245" r="25" fill="var(--rim)"/>
        <circle cx="258" cy="245" r="8" fill="#8d8f91"/>
      </g>
      <g class="wheel">
        <circle cx="730" cy="245" r="42" fill="var(--tyre)"/>
        <circle cx="730" cy="245" r="25" fill="var(--rim)"/>
        <circle cx="730" cy="245" r="8" fill="#8d8f91"/>
      </g>
    </g>

    <g id="wrap-graphics">
      <polygon class="band-light" points="100,128 860,200 860,208 100,136" fill="#d5d7d8"/>
      <polygon class="band-service" points="100,136 860,208 860,240 100,170" fill="var(--gray)"/>
      <polygon class="band-teal-low" points="100,170 640,221 640,260 100,260" fill="var(--teal)"/>
      <polygon class="band-stripe" points="100,172 860,244 860,250 100,178" fill="#ffffff" opacity="0.8"/>
      <g class="service-list" transform="rotate(5.4 172 150)">
        <text class="service" x="172" y="150" textLength="96" lengthAdjust="spacingAndGlyphs">MAINTENANCE &amp; REPAIR</text>
        <text class="service" x="280" y="150" textLength="84" lengthAdjust="spacingAndGlyphs">OIL CHANGE &amp; LUBE</text>
        <text class="service" x="376" y="150" textLength="98" lengthAdjust="spacingAndGlyphs">SLIDE OUTS &amp; AWNINGS</text>
        <text class="service" x="486" y="150" textLength="64" lengthAdjust="spacingAndGlyphs">TIRES &amp; BRAKES</text>
        <text class="service" x="228" y="162" textLength="80" lengthAdjust="spacingAndGlyphs">RV SPA &amp; DETAILING</text>
        <text class="service" x="320" y="162" textLength="76" lengthAdjust="spacingAndGlyphs">LEVELING SYSTEMS</text>
        <text class="service" x="408" y="162" textLength="56" lengthAdjust="spacingAndGlyphs">AC &amp; HEATING</text>
      </g>
      <circle class="brand-dot" cx="236" cy="92" r="34" fill="var(--teal)"/>
      <text class="brand-name" x="284" y="106" font-size="42">BROOKVALE</text>
      <text class="brand-name" x="286" y="138" font-size="24">RV REPAIR &amp; SPA</text>
      <g class="contact" transform="rotate(4 582 160)">
        <text class="phone" x="582" y="162">(888) 514-2089</text>
        <text class="website" x="584" y="176">www.brookvalerv.example</text>
      </g>
    </g>
  </defs>

  <g class="van van-white-teal" transform="translate(0,0)">
    <g clip-path="url(#van-body)">
      <rect x="100" y="40" width="760" height="220" fill="var(--white)"/>
      <polygon points="100,40 760,40 700,62 100,64" fill="var(--teal)"/>
      <use href="#door-seams"/>
      <use href="#wrap-graphics"/>
    </g>
    <use href="#body-outline"/>
    <use href="#van-hardware"/>
  </g>

  <g class="van van-white-gray" transform="translate(0,310)">
    <g clip-path="url(#van-body)">
      <rect x="100" y="40" width="760" height="220" fill="var(--white)"/>
      <polygon points="100,40 760,40 700,62 100,64" fill="var(--gray)"/>
      <use href="#door-seams"/>
      <use href="#wrap-graphics"/>
    </g>
    <use href="#body-outline"/>
    <use href="#van-hardware"/>
  </g>

  <g class="van van-dark" transform="translate(0,624)">
    <g clip-path="url(#van-body)">
      <rect x="100" y="40" width="760" height="220" fill="var(--black)"/>
      <polygon points="100,40 760,40 700,62 100,64" fill="var(--teal)"/>
      <use href="#door-seams"/>
      <use href="#wrap-graphics"/>
    </g>
    <use href="#body-outline"/>
    <use href="#van-hardware"/>
  </g>
</svg>
</body>
</html>
```